Kestrel Bread Ingredients

Ingredients list/einkorn info. We are looking to improve a 5.5 x 8.5" double sided handout (2 per 8.5 x 11" piece of paper) to hand out with bread and for marketing. Or skinnier 3 per piece of paper? Or suggest a better format. Also to be used in social media and web. And possibly a banner.

Target Market(s)

Healthy, intelligent, yoga, athletic, wealthy

Industry/Entity Type

Bakery

Font styles to use
Sans Serif
Other font styles liked:
• simple readable attractive

Requirements
Must have
• Display the value (and uniqueness) of ingredients
Nice to have
• Well presented info with instant visual appeal. Choose between the 2 logos which you like most. Let us know if you want more photos.
Should not have
• Ornate frills

```html
<!DOCTYPE html>
<html lang="en">
<head>
<meta charset="utf-8">
<title>Kestrel Bread – Ingredients &amp; Einkorn</title>
<link href="https://fonts.googleapis.com/css2?family=Questrial&display=swap" rel="stylesheet">
<style>
:root{
  --maroon:#7f2c37;
  --maroon-text:#8a2b3c;
  --orange-a:#f6ad2c;
  --orange-b:#fbb93f;
  --green:#4ca649;
  --beige:#f1dfbf;
  --ink:#1c1a1a;
  --white:#ffffff;
  --ring-shadow:rgba(60,40,20,.22);
  --crust-a:#c99663;
  --crust-b:#7c5232;
  --wheat:#d9953c;
}
*{margin:0;padding:0;box-sizing:border-box}
html,body{width:1200px;height:3106px;overflow:hidden;background:var(--white)}
body{position:relative;font-family:"Questrial",sans-serif;color:var(--ink)}
.abs{position:absolute}
.banner{left:0;width:1200px;background:var(--maroon);color:var(--white);display:flex;align-items:center;justify-content:center;font-size:72px;letter-spacing:.5px}
.banner--top{top:0;height:159px}
.banner--mid{top:1552px;height:142px}
.hero{top:159px;left:0;width:1200px;height:559px;background:linear-gradient(90deg,var(--orange-a),var(--orange-b))}
.hero-photo{top:169px;left:603px;width:597px;height:549px;background:radial-gradient(ellipse at 55% 45%,#f3d9c2 0%,#e9bf8c 40%,rgba(251,185,63,0) 75%)}
.benefits{top:208px;left:136px;list-style:none}
.benefits li{display:flex;gap:22px;color:var(--maroon-text);font-size:38px;line-height:47px;margin-bottom:24px}
.benefits svg{flex:none;width:48px;height:48px}
.benefits small{display:block;font-size:33px}
.tick{width:100%;height:100%}
.loaf-row{left:0;width:1200px;height:260px}
.loaf{position:absolute;width:248px;height:248px;border-radius:50%;background:var(--white);box-shadow:0 14px 22px var(--ring-shadow);padding:8px}
.loaf span{display:block;width:100%;height:100%;border-radius:50%;background:radial-gradient(circle at 50% 50%,var(--crust-a) 0%,#e9d2b3 55%,#efe2cf 70%)}
.loaf.dark span{background:radial-gradient(circle at 50% 50%,var(--crust-b) 0%,#a97a4e 45%,#efe2cf 70%)}
.col{top:870px}
.col h3{font-weight:400;font-size:32px;color:var(--maroon-text);line-height:40px;margin-bottom:4px}
.col ul{list-style:none;font-size:28.5px;line-height:39px}
.col li{padding-left:22px;text-indent:-22px}
.col li::before{content:"• "}
.col p{color:var(--maroon-text);font-size:28.5px;line-height:35px;margin-top:14px}
.with{top:1288px;left:86px;width:740px;font-size:28.5px;line-height:40px}
.with h4{font-weight:400;color:var(--maroon-text);font-size:28.5px;margin-bottom:2px}
.contact{left:86px;font-size:36px}
.contact--top{top:1442px;color:var(--maroon-text)}
.brand{width:296px;height:296px;border-radius:50%;border:4px solid var(--maroon);display:flex;align-items:center;justify-content:center;color:var(--maroon);font-size:36px}
.panel{top:1731px;left:157px;width:886px;height:360px;background:var(--beige);border-radius:30px 30px 0 0;text-align:center;padding-top:40px}
.panel .lead{font-size:47px;line-height:59px;color:var(--maroon-text);width:700px;margin:0 auto}
.panel .note{font-size:33px;line-height:43px;width:700px;margin:22px auto 0}
.wheat{top:1749px;width:187px;height:331px;background:linear-gradient(180deg,rgba(217,149,60,.15),var(--wheat) 60%,rgba(217,149,60,.3));border-radius:90px 90px 10px 10px}
.facts{top:2352px;left:86px;width:1040px}
.facts h4{font-weight:400;color:var(--maroon-text);font-size:32px;margin-bottom:12px}
.facts ul{list-style:none;font-size:32px;line-height:51px}
.facts li{display:flex;gap:14px}
.facts li svg{flex:none;width:27px;height:27px;margin-top:12px}
.cta{top:2944px;left:86px;font-size:38px;color:var(--maroon-text)}
.contact--bottom{top:3000px;color:var(--ink);font-size:38px}
</style>
</head>
<body>

<header class="abs banner banner--top">The Transformation Of Bread</header>

<section class="abs hero"></section>
<div class="abs hero-photo" role="img" aria-label="Smiling woman winking and making an OK hand sign"></div>

<ul class="abs benefits">
  <li><svg viewBox="0 0 48 48"><circle cx="24" cy="24" r="24" fill="var(--green)"/><path d="M13 25l8 8 15-16" stroke="#fff" stroke-width="6" fill="none" stroke-linecap="round" stroke-linejoin="round"/></svg><span>Nutritious • Digestible • Delicious</span></li>
  <li><svg viewBox="0 0 48 48"><circle cx="24" cy="24" r="24" fill="var(--green)"/><path d="M13 25l8 8 15-16" stroke="#fff" stroke-width="6" fill="none" stroke-linecap="round" stroke-linejoin="round"/></svg><span>An Alternative To The Mutated<br>Genetics Of Modern Wheat</span></li>
  <li><svg viewBox="0 0 48 48"><circle cx="24" cy="24" r="24" fill="var(--green)"/><path d="M13 25l8 8 15-16" stroke="#fff" stroke-width="6" fill="none" stroke-linecap="round" stroke-linejoin="round"/></svg><span>Well Tolerated By People<br>With Gluten Sensitivities<small>(not for celiac disease)</small></span></li>
</ul>

<div class="abs loaf-row" style="top:585px">
  <div class="loaf" style="left:65px"><span role="img" aria-label="Slice of marbled einkorn bread"></span></div>
  <div class="loaf dark" style="left:340px"><span role="img" aria-label="Slice of blueberry seed loaf"></span></div>
  <div class="loaf" style="left:615px"><span role="img" aria-label="Stacked slices of swirled bread"></span></div>
  <div class="loaf dark" style="left:889px"><span role="img" aria-label="Round dark sourdough loaf"></span></div>
</div>

<div class="abs col" style="left:86px;width:400px">
  <h3>SPROUTED GRAINS:</h3>
  <ul><li>Einkorn</li><li>Spelt</li><li>Touch of Heritage Rye</li></ul>
  <p>(Organically grown on<br>family farms in Winthrop,<br>Washington &amp; Teton<br>Valley, Idaho)</p>
</div>
<div class="abs col" style="left:500px;width:360px">
  <h3>SEEDS:</h3>
  <ul><li>Amaranth</li><li>Sprouted Pumpkin<br>Seeds</li><li>Sprouted Quinoa</li><li>Chia Seeds</li><li>Flaxseed</li><li>Hemp Hearts</li><li>Sprouted Sunflowers<br>Seeds</li></ul>
</div>
<div class="abs col" style="left:882px;width:300px">
  <h3>ADAPTOGENS:</h3>
  <ul><li>Ashwaganda</li><li>Maca Root</li></ul>
  <h3 style="margin-top:14px">MUSHROOM<br>EXTRACTS:</h3>
  <ul><li>Lion’s Mane</li><li>Cordycept</li></ul>
</div>

<div class="abs with">
  <h4>With:</h4>
  Montana Glacier Well Water, Cacao, MCT Oil, Psyllium Husk, Himalayan Sea Salt, Trace Minerals, Love
</div>
<div class="abs contact contact--top">hello@kestrelbread.com • 406-555-0148</div>
<div class="abs brand" style="left:838px;top:1203px">Kestrel Bread</div>

<header class="abs banner banner--mid">Einkorn Grain Vs ‘Modern Wheat’</header>

<div class="abs wheat" style="left:30px" role="img" aria-label="Golden wheat stalk illustration"></div>
<div class="abs wheat" style="left:983px" role="img" aria-label="Golden wheat stalk illustration"></div>
<section class="abs panel">
  <p class="lead">Einkorn is the original, non-altered wheat grain. It’s genetic purity is over 10,000 years old.</p>
  <p class="note">Einkorn lacks the gluten proteins that trigger symptoms of gluten sensitivity.</p>
</section>

<div class="abs loaf-row" style="top:2081px">
  <div class="loaf" style="left:65px"><span role="img" aria-label="Slice of marbled einkorn bread"></span></div>
  <div class="loaf dark" style="left:340px"><span role="img" aria-label="Slice of blueberry seed loaf"></span></div>
  <div class="loaf" style="left:615px"><span role="img" aria-label="Stacked slices of swirled bread"></span></div>
  <div class="loaf dark" style="left:889px"><span role="img" aria-label="Round dark sourdough loaf"></span></div>
</div>

<section class="abs facts">
  <h4>Einkorn is:</h4>
  <ul>
    <li><svg viewBox="0 0 48 48"><circle cx="24" cy="24" r="24" fill="var(--green)"/><path d="M13 25l8 8 15-16" stroke="#fff" stroke-width="7" fill="none" stroke-linecap="round" stroke-linejoin="round"/></svg><span>25% higher in protein &amp; lower in carbohydrates than modern wheat</span></li>
    <li><svg viewBox="0 0 48 48"><circle cx="24" cy="24" r="24" fill="var(--green)"/><path d="M13 25l8 8 15-16" stroke="#fff" stroke-width="7" fill="none" stroke-linecap="round" stroke-linejoin="round"/></svg><span>3-4 times more beta-carotene</span></li>
    <li><svg viewBox="0 0 48 48"><circle cx="24" cy="24" r="24" fill="var(--green)"/><path d="M13 25l8 8 15-16" stroke="#fff" stroke-width="7" fill="none" stroke-linecap="round" stroke-linejoin="round"/></svg><span>2 times more vitamin A</span></li>
    <li><svg viewBox="0 0 48 48"><circle cx="24" cy="24" r="24" fill="var(--green)"/><path d="M13 25l8 8 15-16" stroke="#fff" stroke-width="7" fill="none" stroke-linecap="round" stroke-linejoin="round"/></svg><span>4 times more antioxidants lutein &amp; riboflavin</span></li>
    <li><svg viewBox="0 0 48 48"><circle cx="24" cy="24" r="24" fill="var(--green)"/><path d="M13 25l8 8 15-16" stroke="#fff" stroke-width="7" fill="none" stroke-linecap="round" stroke-linejoin="round"/></svg><span>5-6 times more expensive</span></li>
    <li><svg viewBox="0 0 48 48"><circle cx="24" cy="24" r="24" fill="var(--green)"/><path d="M13 25l8 8 15-16" stroke="#fff" stroke-width="7" fill="none" stroke-linecap="round" stroke-linejoin="round"/></svg><span>Richer in carotenoids, B vitamins, &amp; essential/ trace minerals</span></li>
    <li><svg viewBox="0 0 48 48"><circle cx="24" cy="24" r="24" fill="var(--green)"/><path d="M13 25l8 8 15-16" stroke="#fff" stroke-width="7" fill="none" stroke-linecap="round" stroke-linejoin="round"/></svg><span>Non-processed, non-hybridized, non-GMO, non- mutated &amp;<br>has a low glycemic load, meaning it won’t spike<br>your blood sugar level</span></li>
    <li><svg viewBox="0 0 48 48"><circle cx="24" cy="24" r="24" fill="var(--green)"/><path d="M13 25l8 8 15-16" stroke="#fff" stroke-width="7" fill="none" stroke-linecap="round" stroke-linejoin="round"/></svg><span>It tastes better</span></li>
  </ul>
</section>

<div class="abs cta">Get in touch for more info!</div>
<div class="abs contact contact--bottom">hello@kestrelbread.com • 406-555-0148</div>
<div class="abs brand" style="left:838px;top:2768px">Kestrel Bread</div>

</body>
</html>
```